Website Design for Business Law Firm

We have a logo and now we would like a web site design for our new website. Our small firm provides creative and aggressive transactional (not litigation) legal services to advise healthcare, technology, internet-based and traditional companies and investors in such companies on healthcare, technology, financing, mergers/acquisitions, real estate and other transactions, legal compliance and general corporate and business matters.

We would like to see a website design that is professional and appropriate for executives, professionals, investors and government regulators to visit, that conveys professionalism and competence while being a little edgy and modern - no typical legal motifs such as gavels, books, or scales of justice. We advise businesses and investors and guide them through complicated issues quickly, capably and differently from other law firms. We are part of the business team and get things done.

The logo is attached, and we like gray as a color to complement it. The intention of the logo is to convey that in a storm or challenging time, people come to this firm, and people come to this firm when they need the power and disruption to change things or shake them up.

I have also enclosed a picture of our business card for consideration.

On the other hand, you can check out the current simple site at www.venhollow.example to see we have used a space motif in the past to evoke that we help create stars (the nebula featured there). This is not a necessary part of the new website and it may look better without it.

We appreciate your creativity and look forward to designs.

Industry/Entity Type

Business

Requirements
Must have
• We anticipate the following pages, and you may submit different ideas for the different pages:
• 1. Landing page
• 2. Services pages - healthcare, IT/Technology, general counsel services, financings, mergers/acquisitions, mediation/arbitration, procurement and productization
• 3. About Us including contact information
• Our name and contact information:
• Quellane Law Firm, P.C.
• 8716 SW 19th Ave.
• Portland, OR 97213
• phone: 971.555.0143
• fax: 971.555.0187
Nice to have
• Please consider designs that enhance the impressions we are looking for
Should not have
• Please no gavels, scales of justice, law books, or similar traditional legal imagery.

```html
<!DOCTYPE html>
<html lang="en">
<head>
<meta charset="utf-8">
<title>Quellane Law Firm, P.C.</title>
<link href="https://fonts.googleapis.com/css2?family=Carlito:wght@400;700&display=swap" rel="stylesheet">
<style>
:root{
  --space-deep:#0a1326;
  --space-mid:#24345a;
  --space-glow:#5a6f99;
  --black:#000;
  --slate:#4f6b78;
  --slate-light:#5d7986;
  --teal-box:#0f3a52;
  --teal-field:#0a2f44;
  --teal-dark:#062233;
  --dot-active:#1e6fa8;
  --dot:#7a8a93;
  --footer:#232323;
  --footer-head:#4f7a8a;
  --text:#ffffff;
  --muted:#cfd6da;
  --welcome-a:#2f3f86;
  --welcome-b:#4f5aa3;
  --welcome-c:#5a4e8e;
}
*{margin:0;padding:0;box-sizing:border-box}
html,body{width:958px;height:1200px;overflow:hidden;background:var(--black)}
body{font-family:"Carlito",Calibri,sans-serif;color:var(--text);position:relative}
.space-band{position:absolute;left:0;top:0;width:958px;height:420px;
  background:radial-gradient(ellipse at 25% 20%,var(--space-glow) 0%,transparent 40%),
  radial-gradient(ellipse at 90% 10%,var(--space-glow) 0%,transparent 35%),
  radial-gradient(ellipse at 10% 70%,var(--space-mid) 0%,transparent 45%),
  linear-gradient(180deg,var(--space-deep) 0%,var(--space-mid) 60%,var(--black) 100%)}
.abs{position:absolute}
.brand{left:152px;top:40px;width:168px;height:40px;display:flex;align-items:center;gap:8px;font-size:26px;letter-spacing:6px;color:var(--text)}
.brand-mark{width:12px;height:12px;background:var(--text)}
.contact-line{right:158px;top:44px;text-align:right}
.contact-line small{display:block;font-size:8.5px}
.contact-line strong{display:block;font-size:19px;font-weight:700;margin-top:1px}
.main-nav{left:150px;top:90px;width:656px;height:40px;background:var(--slate);list-style:none}
.main-nav li{position:absolute;top:13px;font-size:10.5px;font-weight:700}
.hero{left:150px;top:141px;width:656px;height:254px;background:linear-gradient(160deg,#7fb0dc 0%,#c9c2b3 45%,#4d6b3a 100%)}
.hero-caption{left:178px;top:326px;font-size:18px;color:var(--slate)}
.hero-dots{left:176px;top:360px;display:flex;gap:3px}
.hero-dots span{width:8px;height:8px;border-radius:50%;background:var(--dot)}
.hero-dots span:first-child{background:var(--dot-active)}
.section-title{font-size:15.5px;font-weight:400}
.welcome-title{left:152px;top:414px}
.city-photo{left:150px;top:442px;width:431px;height:149px;background:linear-gradient(135deg,var(--welcome-a) 0%,var(--welcome-b) 55%,var(--welcome-c) 100%)}
.intro{left:149px;top:602px;width:431px;font-size:8.7px;line-height:14.2px;text-align:justify}
.intro p+p{margin-top:8px}
.quote-title{left:595px;top:414px}
.quote-box{left:594px;top:440px;width:206px;height:243px;background:linear-gradient(180deg,var(--teal-box),#135070 80%,var(--teal-box))}
.field{position:absolute;left:10px;width:186px;height:32px;background:var(--teal-field);font-size:8.5px;padding:12px 6px 0}
.submit{position:absolute;left:60px;top:212px;width:82px;height:25px;border-radius:5px;background:var(--teal-dark);font-size:10.5px;font-weight:700;text-align:center;line-height:25px}
.services-title{left:0;width:958px;top:720px;text-align:center}
.service{position:absolute;top:751px;width:152px}
.service-photo{width:150px;height:87px}
.service h3{font-size:8.7px;font-weight:700;margin-top:14px}
.service p{font-size:7.3px;line-height:14.4px;text-align:justify;margin-top:5px;padding-left:1px}
.read-more{display:inline-block;margin-top:7px;margin-left:-2px;width:61px;height:22px;background:var(--slate-light);font-size:8.5px;text-align:center;line-height:22px;color:var(--muted)}
.site-footer{left:0;top:998px;width:958px;height:202px;background:var(--footer)}
.foot-col{position:absolute;top:28px}
.foot-col h4{font-size:8.7px;font-weight:400;color:var(--footer-head)}
.foot-col ul{list-style:none;margin-top:14px}
.foot-col li{font-size:7.3px;height:16.4px}
.newsletter p{font-size:7.3px;line-height:13.5px;margin-top:12px;width:152px}
.newsletter .input{width:151px;height:18px;background:#fff;color:#bbb;font-size:6.5px;padding:5px 9px;margin-top:8px}
.newsletter .input+.input{margin-top:11px}
.subscribe{margin:7px 0 0 85px;width:66px;height:16px;border-radius:8px;background:var(--slate-light);font-size:7.3px;font-weight:700;text-align:center;line-height:16px}
.social{list-style:none;margin-top:12px;width:90px}
.social li{display:flex;align-items:center;justify-content:space-between;height:26px;font-size:7.3px}
.social li span{width:19px;height:19px;border-radius:50%;background:#fff}
.copyright{left:0;width:958px;top:1172px;text-align:center;font-size:7.3px}
</style>
</head>
<body>
<div class="space-band"></div>

<header>
  <div class="abs brand"><span class="brand-mark"></span>QUELLANE</div>
  <div class="abs contact-line"><small>Our phone and fax number</small><strong>971.555.0187</strong></div>
  <ul class="abs main-nav">
    <li style="left:22px">HOME</li>
    <li style="left:79px">ABOUT US</li>
    <li style="left:144px">SERVICES</li>
    <li style="left:208px">TESTIMONIALS</li>
    <li style="left:300px">LAW</li>
    <li style="left:339px">FAQ'S</li>
    <li style="left:381px">CONTACT US</li>
  </ul>
</header>

<div class="abs hero" role="img" aria-label="Real estate agent in a suit standing in front of a suburban house"></div>
<div class="abs hero-caption">Real Estate</div>
<div class="abs hero-dots"><span></span><span></span><span></span><span></span></div>

<h2 class="abs section-title welcome-title">Welcome to Quellane</h2>
<div class="abs city-photo" role="img" aria-label="City skyline at dusk reflected in water"></div>
<div class="abs intro">
  <p>Sed ut perspiciatis unde omnis iste natus error sit voluptatem accusantium doloremque laudantium, totam rem aperiam, eaque ipsa quae ab illo inventore veritatis et quasi architecto beatae vitae dicta sunt explicabo.</p>
  <p>Nemo enim ipsam voluptatem quia voluptas sit aspernatur aut odit aut fugit, sed quia consequuntur magni dolores eos qui ratione voluptatem sequi nesciunt. Neque porro quisquam est, qui dolorem ipsum quia dolor sit amet, consectetur, adipisci velit, sed quia non numquam eius modi tempora incidunt ut labore et dolore magnam aliquam quaerat voluptatem.</p>
</div>

<h2 class="abs section-title quote-title">Get a quote</h2>
<form class="abs quote-box">
  <div class="field" style="top:19px">Name</div>
  <div class="field" style="top:61px">e-mail</div>
  <div class="field" style="top:102px">Phone</div>
  <div class="field" style="top:144px;height:59px;padding-top:9px">Message</div>
  <div class="submit">SUBMIT</div>
</form>

<h2 class="abs section-title services-title">Our Services</h2>
<section>
  <div class="service" style="left:157px">
    <div class="service-photo" role="img" aria-label="Smiling woman with fresh fruit" style="background:linear-gradient(160deg,#e9e2c6,#c8b06a 60%,#7aa040)"></div>
    <h3>Healthcare</h3>
    <p>Nemo enim ipsam voluptatem quia voluptas sit aspernatur aut odit aut fugit, sed quia consequuntur magni dolores eos qui ratione voluptatem sequi nesciunt.</p>
    <span class="read-more">Read More</span>
  </div>
  <div class="service" style="left:322px">
    <div class="service-photo" role="img" aria-label="Businessman using a glowing digital interface" style="background:linear-gradient(135deg,#0c3a8a,#1e74c8 55%,#0a1f55)"></div>
    <h3>Technology</h3>
    <p>Nemo enim ipsam voluptatem quia voluptas sit aspernatur aut odit aut fugit, sed quia consequuntur magni dolores eos qui ratione voluptatem sequi nesciunt.</p>
    <span class="read-more">Read More</span>
  </div>
  <div class="service" style="left:486px">
    <div class="service-photo" role="img" aria-label="Calculator, coins and financial charts" style="background:linear-gradient(135deg,#5a6f8a,#c9d4e2 55%,#8a9db5)"></div>
    <h3>Financing</h3>
    <p>Nemo enim ipsam voluptatem quia voluptas sit aspernatur aut odit aut fugit, sed quia consequuntur magni dolores eos qui ratione voluptatem sequi nesciunt.</p>
    <span class="read-more">Read More</span>
  </div>
  <div class="service" style="left:650px">
    <div class="service-photo" role="img" aria-label="Business handshake between office towers" style="background:linear-gradient(135deg,#2b3440,#b8c2cc 50%,#3a3f46)"></div>
    <h3>Mergers/Acquisitions</h3>
    <p>Nemo enim ipsam voluptatem quia voluptas sit aspernatur aut odit aut fugit, sed quia consequuntur magni dolores eos qui ratione voluptatem sequi nesciunt.</p>
    <span class="read-more">Read More</span>
  </div>
</section>

<footer class="abs site-footer">
  <div class="foot-col" style="left:157px">
    <h4>Quick Links</h4>
    <ul><li>Home</li><li>About Us</li><li>Services</li><li>Service Plans</li><li>News</li><li>FAQ &amp; Wiki</li><li>Contact Us</li></ul>
  </div>
  <div class="foot-col" style="left:322px">
    <h4>Support Links</h4>
    <ul><li>Legal Notice</li><li>Privacy Policy</li><li>Terms &amp; Conditions</li><li>Help</li></ul>
  </div>
  <div class="foot-col newsletter" style="left:487px">
    <h4>Newsletter SignUp</h4>
    <p>Sign-up for our daily emails by entering your information below:</p>
    <div class="input">Name</div>
    <div class="input">Enter Your E-Mail ID</div>
    <div class="subscribe">Subscribe</div>
  </div>
  <div class="foot-col" style="left:705px">
    <h4>Connect With Us</h4>
    <ul class="social">
      <li><span></span>Chirpline</li>
      <li><span></span>Friendwall</li>
      <li><span></span>Linkpost</li>
    </ul>
  </div>
</footer>
<div class="abs copyright">Copyright ©2013 Company Name &nbsp; - All rights reserved</div>
</body>
</html>
```